Velmarine - Mechanic/Collision Center Business Card

We're looking for a business card design for our mechanic/ collision repair shop.

Can be with colours or monochromatic.

See the attached files.

Many thanks

```html
<!DOCTYPE html>
<html lang="pt">
<head>
<meta charset="utf-8">
<title>Velmarine – Business Card</title>
<link rel="stylesheet" href="https://fonts.googleapis.com/css2?family=Roboto:wght@400;500;900&display=swap">
<style>
  :root {
    --stage: #e6e8eb;
    --card: #ffffff;
    --brand-blue: #2a95d8;
    --ink: #1c1d1f;
    --text-grey: #55585c;
  }
  html, body {
    margin: 0;
    padding: 0;
    width: 1200px;
    height: 913px;
    overflow: hidden;
    background: var(--stage);
    font-family: "Roboto", Arial, sans-serif;
  }
  .canvas {
    position: relative;
    width: 1200px;
    height: 913px;
  }
  .card {
    position: absolute;
    width: 540px;
    height: 310px;
    background: var(--card);
    border-radius: 22px;
    box-shadow: 0 10px 28px rgba(0,0,0,0.12);
    overflow: hidden;
  }
  .card--front { left: 60px; top: 90px; }
  .card--back { left: 600px; top: 510px; }

  /* brand lockup */
  .brand {
    position: absolute;
    display: flex;
    align-items: center;
    gap: 12px;
    white-space: nowrap;
  }
  .brand__mark {
    width: 30px;
    height: 30px;
    border-radius: 50%;
    background: var(--brand-blue);
    flex: none;
  }
  .brand__name {
    font-weight: 900;
    color: var(--ink);
    text-transform: uppercase;
    letter-spacing: 1px;
    line-height: 1;
  }
  .card--front .brand { left: 44px; bottom: 52px; }
  .card--front .brand__name { font-size: 40px; }

  .card--back .brand { left: 36px; top: 139px; gap: 10px; }
  .card--back .brand__mark { width: 28px; height: 28px; border-radius: 4px; }
  .card--back .brand__name { font-size: 30px; color: var(--brand-blue); letter-spacing: 0.5px; }

  .divider {
    position: absolute;
    left: 290px;
    top: 70px;
    width: 1.5px;
    height: 170px;
    background: var(--brand-blue);
  }
  .contact {
    position: absolute;
    left: 310px;
    top: 70px;
    font-size: 14.5px;
    line-height: 22px;
    color: var(--text-grey);
    white-space: nowrap;
  }
  .contact__company { color: var(--brand-blue); font-weight: 500; margin: 0; }
  .contact__address { margin: 0 0 2px; }
  .contact__list { list-style: none; margin: 0; padding: 0; }
  .contact__list li { display: flex; align-items: center; gap: 8px; }
  .contact__list svg { width: 14px; height: 14px; fill: var(--brand-blue); flex: none; }
  .icon-square { width: 13px; height: 13px; border-radius: 3px; background: var(--brand-blue); flex: none; }
</style>
</head>
<body>
<main class="canvas">
  <section class="card card--front" aria-label="Card front">
    <div class="brand">
      <span class="brand__mark"></span>
      <span class="brand__name">Velmarine</span>
    </div>
  </section>

  <section class="card card--back" aria-label="Card back">
    <div class="brand">
      <span class="brand__mark"></span>
      <span class="brand__name">Velmarine</span>
    </div>
    <div class="divider"></div>
    <div class="contact">
      <p class="contact__company">Velmarine, LDA</p>
      <p class="contact__address">Rua das Oficinas, 42<br>4470-210 Maresol</p>
      <ul class="contact__list">
        <li>
          <svg viewBox="0 0 24 24" aria-hidden="true"><path d="M6.6 10.8a15 15 0 0 0 6.6 6.6l2.2-2.2a1 1 0 0 1 1-.25 11.4 11.4 0 0 0 3.6.57 1 1 0 0 1 1 1V20a1 1 0 0 1-1 1A17 17 0 0 1 3 4a1 1 0 0 1 1-1h3.5a1 1 0 0 1 1 1c0 1.25.2 2.45.57 3.6a1 1 0 0 1-.25 1z"/></svg>
          +351 210 555 482
        </li>
        <li>
          <svg viewBox="0 0 24 24" aria-hidden="true"><path d="M2 5h20v14H2z M3.5 6.5 12 12.5l8.5-6" fill="none" stroke="#2a95d8" stroke-width="2"/><path d="M2 5h20L12 12z"/></svg>
          velmarine.mail@postlane.pt
        </li>
        <li>
          <span class="icon-square"></span>
          velmarine-auto.pt/oficina
        </li>
      </ul>
    </div>
  </section>
</main>
</body>
</html>
```